Lantern Keepers Lantern Scribes

We would like the business card to be Horizontal
Logo on the back and want it raised.

Target Market(s)

Education and Museums

Industry/Entity Type

Education

Contact Information for Business Card

Dolores Wrenfield, P.H.D.
3918 Pelham Rd
Laurel, MD 20799
612.447.3095
Dolores.Wrenfield@lanternkeeperslanternscribes.org
lanternkeeperslanternscribes.org

Font styles to use
Serif

Colors

Designer to choose colors to be used in the design.

Requirements
Must have
• letters and logo must be raised
• Must be slate blue card
• Silver is aluminum foil

```html
<!DOCTYPE html>
<html lang="en">
<head>
<meta charset="utf-8">
<title>Lantern Keepers Lantern Scribes — Business Card</title>
<link rel="stylesheet" href="https://fonts.googleapis.com/css2?family=Montserrat:wght@400;700&display=swap">
<style>
  :root {
    --backdrop: #3a3a3d;
    --slate-deep: #232a58;
    --slate-bright: #0a8ac8;
    --silver: #d9dde2;
    --ink: #111111;
    --paper: #ffffff;
  }
  * { margin: 0; padding: 0; box-sizing: border-box; }
  html, body {
    width: 1200px; height: 1200px; overflow: hidden;
    background: var(--backdrop);
    font-family: "Montserrat", sans-serif;
  }
  .canvas {
    width: 1200px; height: 1200px;
    display: flex; flex-direction: column; align-items: center; justify-content: center;
    gap: 40px;
  }
  .card {
    width: 960px; height: 549px;
    border-radius: 30px;
    position: relative;
    box-shadow: 0 12px 30px rgba(0,0,0,.35);
    overflow: hidden;
  }
  .card--front {
    background: linear-gradient(180deg, var(--slate-deep) 0%, var(--slate-bright) 35%, var(--slate-bright) 50%, var(--slate-deep) 100%);
    display: flex; align-items: center; justify-content: center;
  }
  .front-name {
    color: var(--silver);
    font-weight: 700; font-size: 30px; letter-spacing: 2px;
    text-transform: uppercase; white-space: nowrap;
  }
  .card--back { background: var(--paper); }
  .back-name {
    position: absolute; right: 70px; top: 110px;
    color: var(--ink); font-weight: 700; font-size: 20px;
    letter-spacing: 1px; text-transform: uppercase; white-space: nowrap;
  }
  .contact {
    position: absolute; left: 70px; bottom: 70px;
    color: var(--ink);
  }
  .contact__name {
    font-weight: 700; font-size: 30px; letter-spacing: 1px; text-transform: uppercase;
    margin-bottom: 14px;
  }
  .contact__name small { font-size: 22px; }
  .contact__line {
    font-size: 18px; line-height: 1.45;
    display: flex; align-items: center; gap: 8px;
  }
  .contact__line svg { width: 16px; height: 16px; flex: none; }
  .contact__line--plain { padding-left: 24px; }
</style>
</head>
<body>
<main class="canvas">
  <section class="card card--front" aria-label="Card front">
    <div class="front-name">Lantern Keepers Lantern Scribes</div>
  </section>

  <section class="card card--back" aria-label="Card back">
    <div class="back-name">Lantern Keepers Lantern Scribes</div>
    <div class="contact">
      <div class="contact__name">Dolores Wrenfield, <small>P.H.D.</small></div>
      <div class="contact__line contact__line--plain">3918 Pelham Rd</div>
      <div class="contact__line contact__line--plain">Laurel, MD 20799</div>
      <div class="contact__line">
        <svg viewBox="0 0 16 16"><path d="M3 1.5l3 .5 1 3-1.8 1.4a9 9 0 0 0 4.4 4.4L11 9l3 1 .5 3-2 1.5C7 14 2 9 1.5 3.5z" fill="var(--ink)"/></svg>
        612.447.3095
      </div>
      <div class="contact__line">
        <svg viewBox="0 0 16 16"><rect x="1" y="3.5" width="14" height="9" fill="none" stroke="var(--ink)" stroke-width="1.5"/><path d="M1 3.5l7 5 7-5" fill="none" stroke="var(--ink)" stroke-width="1.5"/></svg>
        Dolores.Wrenfield@lanternkeeperslanternscribes.org
      </div>
      <div class="contact__line">
        <svg viewBox="0 0 16 16"><circle cx="8" cy="8" r="6.5" fill="none" stroke="var(--ink)" stroke-width="1.3"/><ellipse cx="8" cy="8" rx="3" ry="6.5" fill="none" stroke="var(--ink)" stroke-width="1.1"/><path d="M1.5 8h13" stroke="var(--ink)" stroke-width="1.1"/></svg>
        www.lanternkeeperslanternscribes.org
      </div>
    </div>
  </section>
</main>
</body>
</html>
```